KVR bottled water label

We are from The KVR Shop (TKS) - a university campus-retail initiative. As part of our branding exercise, we would like to produce a new range of bottled water and need a new label design carrying the following headline: "U Make A Different U" (primary headline) with "The World Is Your Campus" as the sub-headline (secondary headline).
Usage Of Line:
Emphasis must be given to the primary headline, and must not be placed before or on top of the primary headline. The reader must first read the primary headline before reading the secondary headline (assuming the reader reads from left to right and top to bottom.)
THE CONCEPT BEHIND OUR LINE:
Some Background:
Perceived as a fast-rising star since our inception in 2000, Harbourline Civic University challenged the Singapore education landscape - long dominated by an established field of long-tenured universities – by providing a holistic, broad-based and cross-disciplinary form of education that incorporates global exposure, internships and networking opportunities to prepare our students for real-world challenges - an experiential learning environment which we’ve proudly pioneered. Watch these videos from our graduates sharing their KVR experiences: http://kvr.example/22
When our first batch of graduates started their careers in 2004, employers saw a different breed of leaders. The graduates from KVR were bold, confident, articulate, versatile, well-rounded and eager for challenges. Today, more than 10,000 graduates across the world are testament to our trademark holistic and interactive approach to education. Our graduate employment record has been, and continues to be, robust with 60% finding jobs before graduation, and close to 100% getting employed within six months of graduation. Watch employers from Zentrova, QHL, WEV & LNJ at: http://kvr.example/21
That is why we invite prospective students to Discover A Different 'U' - the letter 'U' can be interpreted to mean the 'U'niversity or 'U' as an individual (the prospective student).
The New Line:
With our new headline "U Make A Different U - The World Is Your Campus", we now pose the challenge back to our prospective students, and invite them to make a difference. How different their university experience can be, and how much they can be transformed, is limited only by their imagination.
For more information on KVR, please visit our website at: kvr.example.edu
Design:
The design must be vibrant and fresh to appeal to our students (from 18 years of age), yet still fit in perfectly on a table for a board of professionals and executive directors.
Audience:
It should appeal to the general masses, from our students to distinguished guests and executive directors to KVR.
Things to include (Requirements):
1. KVR logo (as below) must be included)
https://files.example.net/s/qk41tm8rb2xw/KVR%20Formal%20Logo.zip
2. Only 4 colours can be used (white is considered one color)
3. Must design within perimeters of working file:
https://files.example.net/s/hp73nd5ye9ja/bottled%20water%20working%20file.pdf
References
http://kvr.example/1m
http://kvr.example/1o
http://kvr.example/1p
http://kvr.example/1q
http://kvr.example/1r
http://kvr.example/1s
http://kvr.example/1t
http://kvr.example/1u
http://kvr.example/1v
http://kvr.example/1w
http://kvr.example/1x
http://kvr.example/1y

```html
<!DOCTYPE html>
<html lang="en">
<head>
<meta charset="utf-8">
<title>KVR Bottled Water Label</title>
<link rel="stylesheet" href="https://fonts.googleapis.com/css2?family=Archivo+Black&family=Great+Vibes&family=Arimo:wght@400;700&display=swap">
<style>
  :root {
    --navy: #0b1f3f;
    --blue-deep: #173a6b;
    --blue-mid: #2f6fa8;
    --blue-light: #4f8fc4;
    --magenta: #e0177d;
    --white: #ffffff;
    --ink: #111111;
  }
  * { box-sizing: border-box; margin: 0; padding: 0; }
  html, body { width: 1200px; height: 240px; overflow: hidden; background: var(--white); }
  .label {
    position: relative;
    width: 1200px;
    height: 240px;
    overflow: hidden;
    font-family: "Arimo", Arial, sans-serif;
  }
  .front {
    position: absolute;
    left: 0; top: 0;
    width: 1073px; height: 240px;
    background: radial-gradient(ellipse 55% 110% at 36% 45%, var(--blue-light) 0%, var(--blue-mid) 35%, var(--blue-deep) 70%, var(--navy) 100%);
  }
  .swirl {
    position: absolute;
    top: 0;
    height: 240px;
  }
  .swirl--left {
    left: 0; width: 230px;
    background: linear-gradient(100deg, rgba(224,23,125,0.55) 0%, rgba(255,255,255,0.25) 45%, rgba(11,31,63,0) 100%);
  }
  .swirl--right {
    left: 560px; width: 513px;
    background: linear-gradient(80deg, rgba(11,31,63,0) 0%, rgba(255,255,255,0.18) 45%, rgba(224,23,125,0.5) 100%);
  }
  .brand {
    position: absolute;
    left: 312px; top: 12px;
    display: flex; align-items: center; gap: 7px;
    color: var(--white);
  }
  .brand__mark {
    width: 20px; height: 20px;
    background: var(--white);
  }
  .brand__name {
    font-family: "Arimo", Arial, sans-serif;
    font-weight: 700;
    font-size: 24px;
    letter-spacing: 1px;
    line-height: 1;
  }
  .headline {
    position: absolute;
    left: 190px; top: 66px;
    width: 400px;
    text-align: center;
    white-space: nowrap;
    font-family: "Archivo Black", "Arial Black", sans-serif;
    font-size: 23px;
    font-weight: 400;
    line-height: 1;
    color: var(--white);
    text-shadow: 1px 1px 0 rgba(11,31,63,0.6);
  }
  .subheadline {
    position: absolute;
    left: 190px; top: 92px;
    width: 400px;
    text-align: center;
    white-space: nowrap;
    font-family: "Great Vibes", cursive;
    font-size: 34px;
    line-height: 1;
    color: var(--navy);
    text-shadow: 0 0 3px rgba(255,255,255,0.8);
  }
  .back {
    position: absolute;
    left: 1073px; top: 0;
    width: 127px; height: 240px;
    background: var(--white);
    padding: 6px 5px;
    color: var(--ink);
    font-size: 5.6px;
    line-height: 1.2;
  }
  .back__product {
    font-size: 7px;
    text-align: center;
    margin-bottom: 2px;
  }
  .facts {
    border: 1px solid var(--ink);
    width: 100%;
    border-collapse: collapse;
    table-layout: fixed;
    font-size: 5.6px;
  }
  .facts td, .facts th { padding: 0 2px; font-weight: 400; text-align: left; white-space: nowrap; overflow: hidden; }
  .facts .num { text-align: right; }
  .facts__title {
    font-weight: 700;
    font-size: 7px;
    text-align: center;
    border-bottom: 1px solid var(--ink);
  }
  .facts__head th { border-top: 1px solid var(--ink); border-bottom: 1px solid var(--ink); }
  .back__notes { margin-top: 2px; }
  .back__maker { margin-top: 2px; }
  .back__tech {
    margin-top: 4px;
    font-weight: 700;
    font-size: 6.5px;
    text-align: center;
    white-space: nowrap;
  }
  .back__techline {
    display: flex; align-items: baseline; justify-content: center; gap: 3px;
    margin-top: 1px;
  }
  .back__techname {
    font-family: "Arimo", Arial, sans-serif;
    font-weight: 700;
    font-size: 16px;
    line-height: 1.1;
  }
  .back__origin { font-size: 6px; }
</style>
</head>
<body>
<div class="label">
  <section class="front">
    <div class="swirl swirl--left" role="img" aria-label="Decorative pink, white and navy floral swirls"></div>
    <div class="swirl swirl--right" role="img" aria-label="Decorative pink, white and navy floral swirls"></div>

    <div class="brand">
      <span class="brand__mark"></span>
      <span class="brand__name">KVR</span>
    </div>

    <h1 class="headline">U MAKE A DIFFERENT U</h1>
    <p class="subheadline">The World Is Your Campus</p>
  </section>

  <aside class="back">
    <p class="back__product">Oxygenated Drinking Water</p>
    <table class="facts">
      <colgroup><col style="width:40%"><col style="width:30%"><col style="width:30%"></colgroup>
      <tr><td class="facts__title" colspan="3">Nutrition Information</td></tr>
      <tr><td colspan="2">Serving per package</td><td class="num">500ml</td></tr>
      <tr><td colspan="2">Serving size</td><td class="num">100ml</td></tr>
      <tr class="facts__head"><th></th><th class="num">per serving</th><th class="num">per 100ml</th></tr>
      <tr><td>energy</td><td class="num">0 kcal*</td><td class="num">0 kcal*</td></tr>
      <tr><td>protein</td><td class="num">0 g</td><td class="num">0 g</td></tr>
      <tr><td>total fat</td><td class="num">0 g</td><td class="num">0 g</td></tr>
      <tr><td>carbohydrate</td><td class="num">0 g</td><td class="num">0 g</td></tr>
      <tr><td>sodium</td><td class="num">0 g</td><td class="num">0 g</td></tr>
    </table>
    <p class="back__notes">* 1 kcal = 4.2kJ<br>Not a significant source of dietary fibre, saturated fats and cholesterol.</p>
    <p class="back__maker">Manufactured in Singapore for<br><strong>VANTARO HYDRO SYSTEMS (S) PTE LTD</strong><br>Tel: +65 5550 0123 &nbsp;Fax: +65 5550 0124<br>Email: info@vantaro.example</p>
    <p class="back__tech">Produced Using The Technology of</p>
    <div class="back__techline">
      <span class="back__techname">VANTARO</span>
      <span class="back__origin">Singapore</span>
    </div>
  </aside>
</div>
</body>
</html>
```